Varemo Group Business Card Design

The CEO is looking for a new trendy look for his business card.
You can stay with current branding or come up with something new/creative. It can be 3D, including Medical Office buildings. You can use our logo in a variety of colors. Please include name, title, company name, company website, email address, cell number

Target Market(s)

Real Estate Development and Construction

Industry/Entity Type

Health care real estate

Contact Information for Business Card

Rohesh Kumbar, CEO M-727.418.9062 E-roheshkumbar@varemo.com Address:4100 Lindell Ave, Tampa, FL 33611 www.varemo.com

Font styles to use
Other font styles liked:
• Be creative

Requirements
Must have
• Creative, trendy look
Nice to have
• Please go to our website to get a feel- www. varemo.com
Should not have
• small fonts

```html
<!DOCTYPE html>
<html lang="en">
<head>
<meta charset="utf-8">
<title>Varemo Group Business Card</title>
<link href="https://fonts.googleapis.com/css2?family=Montserrat:wght@400;700;900&display=swap" rel="stylesheet">
<style>
  :root {
    --stage: #2b2b2b;
    --card-black: #0c0c0c;
    --card-white: #ffffff;
    --ink: #111111;
    --ink-soft: #333333;
    --rule: #222222;
  }
  * { margin: 0; padding: 0; box-sizing: border-box; }
  html, body { width: 1200px; height: 875px; overflow: hidden; }
  body {
    background: var(--stage);
    font-family: "Montserrat", sans-serif;
    position: relative;
  }
  .card {
    position: absolute;
    width: 540px;
    height: 310px;
    border-radius: 22px;
    overflow: hidden;
  }
  .card-back {
    left: 50px;
    top: 120px;
    background: var(--card-black);
  }
  .back-texture {
    position: absolute;
    inset: 0;
    background: linear-gradient(100deg, #5a5a5a 0%, #262626 30%, #111111 55%, #0c0c0c 100%);
  }
  .back-name {
    position: absolute;
    right: 70px;
    top: 130px;
    color: #ffffff;
    font-weight: 900;
    font-size: 30px;
    letter-spacing: -0.5px;
  }
  .card-front {
    left: 610px;
    top: 445px;
    background: var(--card-white);
    color: var(--ink);
  }
  .front-name {
    position: absolute;
    right: 34px;
    top: 36px;
    font-weight: 900;
    font-size: 44px;
    letter-spacing: -1px;
    line-height: 1;
  }
  .front-rule {
    position: absolute;
    left: 170px;
    right: 34px;
    top: 112px;
    border-top: 1.2px solid var(--rule);
  }
  .address {
    position: absolute;
    right: 34px;
    top: 124px;
    text-align: right;
    font-size: 12.5px;
    line-height: 1.4;
    color: var(--ink-soft);
  }
  .person {
    position: absolute;
    left: 30px;
    top: 170px;
  }
  .person-name {
    font-weight: 700;
    font-size: 20px;
  }
  .person-title {
    font-size: 13px;
    color: var(--ink-soft);
    margin-top: 2px;
    padding-bottom: 8px;
    border-bottom: 1.2px solid var(--rule);
    width: 175px;
  }
  .contacts {
    list-style: none;
    margin-top: 8px;
  }
  .contacts li {
    display: flex;
    align-items: center;
    gap: 9px;
    font-size: 13px;
    line-height: 22px;
    color: var(--ink-soft);
  }
  .contacts svg { width: 12px; height: 12px; fill: var(--ink); flex: none; }
</style>
</head>
<body>
  <section class="card card-back">
    <div class="back-texture" role="img" aria-label="Repeating glossy brand-name pattern across the black card"></div>
    <div class="back-name">Varemo Group</div>
  </section>

  <section class="card card-front">
    <div class="front-name">Varemo Group</div>
    <div class="front-rule"></div>
    <div class="address">4100 Lindell Ave,<br>Tampa, FL 33611</div>

    <div class="person">
      <div class="person-name">Rohesh Kumbar</div>
      <div class="person-title">CEO</div>
      <ul class="contacts">
        <li>
          <svg viewBox="0 0 24 24"><path d="M6.6 10.8a15.1 15.1 0 0 0 6.6 6.6l2.2-2.2c.3-.3.7-.4 1-.2 1.1.4 2.3.6 3.6.6.6 0 1 .4 1 1V20c0 .6-.4 1-1 1A17 17 0 0 1 3 4c0-.6.4-1 1-1h3.5c.6 0 1 .4 1 1 0 1.3.2 2.5.6 3.6.1.3 0 .7-.2 1z"/></svg>
          727.418.9062
        </li>
        <li>
          <svg viewBox="0 0 24 24"><path d="M2 5h20v14H2z M2 5l10 8 10-8" /></svg>
          roheshkumbar@varemo.com
        </li>
        <li>
          <svg viewBox="0 0 24 24"><circle cx="12" cy="12" r="10"/></svg>
          www.varemo.com
        </li>
      </ul>
    </div>
  </section>
</body>
</html>
```